GUARANTEED Project: Folded Business Card- Brightwave Motion

This project is to design a folded business card for BRIGHTWAVE MOTION; to be used in a business development capacity by the owner. The business card should communicate WHAT Brightwave Motion is and HOW property managers can implement Brightwave Motion at their property, without additive verbal explanation.

As long as it is standard-size, you may use either a horizontal or vertical layout, folded business card. You may use either an even-set or off-set layout, though an even-set layout may give you additional space. You should also considering using the back of the card (possibly for the QR code).

Imagine that you are handed this card by a friend who thought you might be interested in this service. By looking at the front of the card, you have a basic understanding that this business provides fitness-related services for office properties. You are interested because you are a property manager, but wonder how this would really work at your property.

When you look at the inside of the business card, you understand how Brightwave Motion can be offered at your property, easily and with zero cost.

About the Business:
Brightwave Motion provides fun, energizing fitness programming to commercial office and residential communities. Our programs are designed to enhance the participants’ workplace experience and help participants recapture the joy of health. Our mission is to energize communities by making fitness fun, convenient and accessible.

The most universal and recognizable offering in our program is group fitness classes (i.e. yoga, Ravelo, boot camp), held on-site at the office building or apartment complex. The accessibility and convenience of the classes is a key aspect of the business, second only to a commitment to extraordinary fitness programming.

Objective:
A successful b-card design must address both of the following objectives:
1) help the audience immediately connect fitness and commercial office space. A property manager looking at the front of the business card should immediately think “Brightwave Motion at my commercial office property”

2) overcome objections about cost and implementation. A property manager scanning the inside of the business card should understand how simple and low-cost the service is

A company flyer has been uploaded, for reference purposes only.
Updates

Hi Designers,

Please be advised, that the deadline for the project has been moved up by one day to 01/23.  Although the system does not indicated, I assume this end of day 01/23.

My timeline for getting the cards finalized and printed was shortened, which is the reason for moving up the deadline.  I will be available until 4 pm PST tomorrow, in order to give feedbacks and will try to comment on your designs as soon as they are submitted so that you may have some time to make revisions if you choose.

Thank you!
Lira

Target Market(s)

Property managers and owners of both commercial office buildings and residential communities. These are 30- 50 year old semi-professionals.

Industry/Entity Type

Residential

Requirements
Must have
• - Logo
- Contact information
Name: Lira Pembrook
Title: Founder
Phone: 555-304-8817
Email: lira@bwmotionhub.example
URL: www.bwmotionhub.example

The following KEY POINTS SHOULD BE ADDRESSED, whether as text, illustration, image or concept. The points are likely best addressed on the inside of the folded business card.

- On-site fitness is a prestigious amenity for Class A properties (image may be a commercial office building; image provided)

- Fitness classes are held in empty office spaces 1-3 times a week (image may be an empty office; image provided)

- Brightwave Motion is full-service providing all staffing, fitness equipment, and administration

- Zero cost to property; class fees paid by participants fitness class (image may be fitness class; image provided)
Nice to have
• You may use images, text or any combination to communicate the following key points. Some stock photos are provided (print-ready files will be provided when a design has been chosen) but are not required to be in the design. You may use other images, vectors, representations.

```html
<!DOCTYPE html>
<html lang="en">
<head>
<meta charset="utf-8">
<title>Brightwave Motion – Folded Business Card</title>
<link rel="stylesheet" href="https://fonts.googleapis.com/css2?family=Arimo:wght@400;700&family=Source+Sans+3:wght@400&display=swap">
<style>
  :root {
    --sheet: #ffffff;
    --card-dark: #231f20;
    --orange: #f26722;
    --panel-grey: #58595b;
    --white: #ffffff;
    --label: #222222;
    --divider: #d8d8d8;
  }
  * { box-sizing: border-box; margin: 0; padding: 0; }
  html, body { width: 986px; height: 1200px; overflow: hidden; background: var(--sheet); }
  body { position: relative; font-family: "Arimo", Arial, sans-serif; }

  .abs { position: absolute; }

  /* Sheet labels and dimensions */
  .view-label {
    position: absolute; transform: translateX(-50%);
    font-family: "Source Sans 3", "Myriad Pro", sans-serif;
    font-size: 15px; color: var(--label); white-space: nowrap;
  }
  .dimensions { position: absolute; left: 0; top: 0; }
  .dim-text {
    position: absolute; font-family: "Source Sans 3", sans-serif;
    font-size: 15px; color: var(--label);
  }
  .dim-text--height { transform: rotate(-90deg); transform-origin: left top; }

  /* Card surfaces */
  .card-dark { background: var(--card-dark); }
  .card-orange { background: var(--orange); }

  /* Brand lockup */
  .brand-lockup {
    position: absolute; display: flex; align-items: center; gap: 10px;
    transform: translate(-50%, -50%); white-space: nowrap;
  }
  .brand-dot { width: 14px; height: 14px; border-radius: 50%; background: var(--orange); }
  .brand-name {
    font-weight: 700; font-size: 26px; letter-spacing: 1px; color: var(--white);
  }

  /* Vertical contact strip */
  .info-strip { position: absolute; width: 52px; height: 286px; background: var(--orange); }
  .info-strip__inner {
    position: absolute; width: 286px; height: 52px;
    left: -117px; top: 117px; transform: rotate(-90deg);
    display: flex; justify-content: space-between; align-items: center;
    padding: 0 12px; color: var(--white); font-size: 10.5px; line-height: 14px;
  }
  .contact-name { font-weight: 700; font-size: 12px; }

  .website { font-weight: 700; font-size: 15px; color: var(--white); letter-spacing: .2px; }

  /* Inside panel */
  .inside-top { background: var(--panel-grey); }
  .photo { position: absolute; }
  .photo--building { background: linear-gradient(160deg, #2f6fb5 0%, #5b93cf 45%, #9db7cf 75%, #44607d 100%); }
  .photo--class { border-radius: 8px; background: linear-gradient(120deg, #7d8aa0 0%, #d9b49c 40%, #e98bb2 60%, #6c7385 100%); }
  .photo--office { border-radius: 8px; background: linear-gradient(180deg, #e9ecef 0%, #c9ccd0 55%, #8d9094 100%); }
  .point-text { position: absolute; font-size: 13px; line-height: 16px; color: var(--white); }
  .point-text--rule { border-left: 1px solid var(--divider); padding-left: 12px; }
  .point-text--overlay { text-align: right; }
  .service-statement { font-size: 22.5px; line-height: 28px; color: var(--orange); }

  .zero-badge {
    position: absolute; width: 136px; height: 136px; border-radius: 50%;
    background: var(--orange); border: 7px solid var(--white);
    display: flex; flex-direction: column; align-items: center; justify-content: center;
    color: var(--white); text-align: center;
  }
  .zero-badge__lead { font-size: 15px; line-height: 18px; }
  .zero-badge__main { font-weight: 700; font-size: 25px; line-height: 25px; color: var(--card-dark); }
  .zero-badge__tail { font-size: 15px; line-height: 20px; }
</style>
</head>
<body>

  <!-- Dimension marks -->
  <svg class="dimensions" width="986" height="400" aria-hidden="true">
    <line x1="87" y1="58" x2="87" y2="84" stroke="#222" stroke-width="1.5"/>
    <line x1="528" y1="58" x2="528" y2="84" stroke="#222" stroke-width="1.5"/>
    <line x1="56" y1="93" x2="79" y2="93" stroke="#222" stroke-width="1.5"/>
    <line x1="56" y1="378" x2="79" y2="378" stroke="#222" stroke-width="1.5"/>
  </svg>
  <span class="dim-text" style="left:288px; top:60px;">85mm</span>
  <span class="dim-text dim-text--height" style="left:58px; top:258px;">55mm</span>

  <!-- Folded view -->
  <section class="folded-card" aria-label="Folded card">
    <div class="abs card-dark" style="left:86px; top:92px; width:391px; height:286px;"></div>
    <div class="brand-lockup" style="left:281px; top:240px;">
      <span class="brand-dot"></span><span class="brand-name">BRIGHTWAVE MOTION</span>
    </div>
    <div class="info-strip" style="left:477px; top:92px;">
      <div class="info-strip__inner">
        <div><div class="contact-name">Lira Pembrook</div><div>Founder</div></div>
        <div><div>Phone: 555-304-8817</div><div>Email: lira@bwmotionhub.example</div></div>
      </div>
    </div>
  </section>
  <span class="view-label" style="left:300px; top:402px;">Folded</span>

  <!-- Front and back -->
  <section class="front-back" aria-label="Front and back of card">
    <div class="abs card-orange" style="left:85px; top:471px; width:442px; height:286px;"></div>
    <span class="abs website" style="left:217px; top:605px;">www.bwmotionhub.example</span>
    <div class="abs card-dark" style="left:527px; top:471px; width:391px; height:286px;"></div>
    <div class="brand-lockup" style="left:722px; top:620px;">
      <span class="brand-dot"></span><span class="brand-name">BRIGHTWAVE MOTION</span>
    </div>
  </section>
  <span class="view-label" style="left:528px; top:778px;">Front and Back</span>

  <!-- Inside panel -->
  <section class="inside-panel" aria-label="Inside panel">
    <div class="abs inside-top" style="left:86px; top:837px; width:780px; height:195px;"></div>
    <div class="abs card-dark" style="left:86px; top:1032px; width:780px; height:91px;"></div>

    <div class="photo photo--building" role="img" aria-label="Photo of a tall glass office tower against a blue sky" style="left:86px; top:837px; width:237px; height:186px;"></div>
    <p class="point-text point-text--overlay" style="left:150px; top:855px; width:152px;">On-site fitness is a prestigious amenity for Class A properties</p>

    <p class="point-text point-text--rule" style="left:354px; top:855px; width:240px;">Zero cost to property; class fees paid by participants fitness class.</p>
    <div class="photo photo--class" role="img" aria-label="Photo of a group fitness class stretching in a studio" style="left:354px; top:898px; width:234px; height:125px;"></div>

    <p class="point-text point-text--rule" style="left:616px; top:855px; width:240px;">Fitness classes are held in empty office spaces 1-3 times a week.</p>
    <div class="photo photo--office" role="img" aria-label="Photo of an empty, bright office floor with large windows" style="left:616px; top:898px; width:250px; height:125px;"></div>

    <p class="abs service-statement" style="left:168px; top:1048px; width:540px;">Brightwave Motion is full-service providing all staffing, fitness equipment, and administration.</p>

    <div class="zero-badge" style="left:702px; top:992px;">
      <span class="zero-badge__lead">At</span>
      <span class="zero-badge__main">ZERO<br>COST</span>
      <span class="zero-badge__tail">to you!</span>
    </div>

    <div class="info-strip" style="left:866px; top:837px;">
      <div class="info-strip__inner">
        <div><div class="contact-name">Lira Pembrook</div><div>Founder</div></div>
        <div><div>Phone: 555-304-8817</div><div>Email: lira@bwmotionhub.example</div></div>
      </div>
    </div>
  </section>
  <span class="view-label" style="left:528px; top:1148px;">Inside Panel</span>

</body>
</html>
```